Vital Spark Electrical in need of a business card design

We need a new business card designed for our electrical business. We have a logo already which I will attach below.
Would like the business card to be..
-BLACK background preferably, possibly white back ground behind logo if colours clash.
-White & Blue (logo blue) text
Something that makes the logo pop, & a modern look. Possibly minimal clean format.

REQUIRE:
-Logo on front & back

TEXT TO INCLUDE (ON ONE SIDE):

Tom Harlow
Director/Electrician
M: 0417 365 208
E:info@vitalsparkelectrical-example.com.au
W:www.vitalsparkelectrical-example.com.au
R.E.C 57318

Custom/New Homes
Renovations
Commercial Office/Shop Fit-outs
Communications & Security Cameras
Electric Vehicle Chargers
Airconditioning
Updates

Requirements
Nice to have
• Possibly even lighten the grey shades for the words 'Vital' & 'Spark' to be more easily read on a black background.

```html
<!DOCTYPE html>
<html lang="en">
<head>
<meta charset="utf-8">
<title>Vital Spark Electrical – Business Card</title>
<link rel="stylesheet" href="https://fonts.googleapis.com/css2?family=Rubik:wght@400;500&display=swap">
<style>
  :root {
    --page-bg: #1c1c1e;
    --card-bg: #111112;
    --brand-blue: #12b0e8;
    --text-light: #e4e6e8;
    --text-grey: #c3c8ce;
    --divider: #4a4f55;
    --bullet: #7d8288;
  }
  * { margin: 0; padding: 0; box-sizing: border-box; }
  html, body {
    width: 1200px; height: 1200px; overflow: hidden;
    background: var(--page-bg);
    font-family: "Rubik", sans-serif;
  }
  .sheet {
    position: relative; width: 1200px; height: 1200px;
    display: flex; flex-direction: column; align-items: center;
    justify-content: center; gap: 40px;
  }
  .card {
    position: relative; width: 960px; height: 548px;
    background: var(--card-bg);
    box-shadow: 0 14px 30px rgba(0,0,0,.55);
    overflow: hidden;
  }
  .brand {
    position: absolute; display: flex; align-items: center; gap: 16px;
  }
  .brand-mark {
    width: 22px; height: 22px; background: var(--brand-blue);
  }
  .brand-name {
    font-weight: 500; font-size: 34px; color: var(--text-grey);
    letter-spacing: .5px; white-space: nowrap;
  }
  /* services side */
  .card--services .brand { left: 150px; top: 70px; }
  .services {
    position: absolute; left: 130px; top: 200px;
    list-style: none; color: var(--brand-blue);
    font-size: 20px; line-height: 28px; letter-spacing: .6px;
  }
  .services li { position: relative; padding-left: 26px; }
  .services li::before {
    content: ""; position: absolute; left: 0; top: 10px;
    width: 8px; height: 8px; border-radius: 50%; background: var(--bullet);
  }
  /* contact side */
  .card--contact .brand { left: 70px; top: 190px; }
  .card--contact .brand-name { font-size: 30px; }
  .divider {
    position: absolute; left: 500px; top: 150px;
    width: 2px; height: 170px; background: var(--divider);
  }
  .person { position: absolute; left: 540px; top: 150px; }
  .person-name {
    font-weight: 500; font-size: 30px; color: var(--text-grey);
    letter-spacing: 1px; text-transform: uppercase;
  }
  .person-role {
    font-size: 22px; color: var(--brand-blue);
    letter-spacing: .6px; text-transform: uppercase; margin-top: 2px;
  }
  .contacts { list-style: none; margin-top: 18px; }
  .contacts li {
    display: flex; align-items: center; gap: 12px;
    font-size: 18px; color: var(--text-light); letter-spacing: .6px;
    line-height: 32px; white-space: nowrap;
  }
  .contacts svg { width: 20px; height: 20px; flex: none; }
  .accent-line {
    position: absolute; left: 0; bottom: 80px; width: 700px;
    height: 3px; background: var(--brand-blue);
  }
  .accent-line--end { left: auto; right: 0; width: 60px; }
  .licence {
    position: absolute; right: 86px; bottom: 68px;
    font-size: 22px; color: var(--text-light); letter-spacing: .8px;
  }
</style>
</head>
<body>
<main class="sheet">
  <section class="card card--services">
    <div class="brand">
      <span class="brand-mark"></span>
      <span class="brand-name">Vital Spark Electrical</span>
    </div>
    <ul class="services">
      <li>Custom/New Homes</li>
      <li>Renovations</li>
      <li>Commercial Office/Shop Fit-outs</li>
      <li>Communications &amp; Security Cameras</li>
      <li>Electric Vehicle Chargers</li>
      <li>Airconditioning</li>
    </ul>
  </section>

  <section class="card card--contact">
    <div class="brand">
      <span class="brand-mark"></span>
      <span class="brand-name">Vital Spark Electrical</span>
    </div>
    <div class="divider"></div>
    <div class="person">
      <h1 class="person-name">Tom Harlow</h1>
      <p class="person-role">Director/Electrician</p>
      <ul class="contacts">
        <li>
          <svg viewBox="0 0 24 24" aria-hidden="true"><path fill="#12b0e8" d="M6.6 10.8a15.1 15.1 0 0 0 6.6 6.6l2.2-2.2a1 1 0 0 1 1-.25 11.4 11.4 0 0 0 3.6.57 1 1 0 0 1 1 1V20a1 1 0 0 1-1 1A17 17 0 0 1 3 4a1 1 0 0 1 1-1h3.5a1 1 0 0 1 1 1c0 1.25.2 2.45.57 3.57a1 1 0 0 1-.25 1z"/></svg>
          0417 365 208
        </li>
        <li>
          <svg viewBox="0 0 24 24" aria-hidden="true"><rect x="2" y="5" width="20" height="14" fill="#12b0e8"/><path d="M2 5l10 8 10-8" fill="none" stroke="#111112" stroke-width="1.6"/></svg>
          info@vitalsparkelectrical-example.com.au
        </li>
        <li>
          <svg viewBox="0 0 24 24" aria-hidden="true"><g fill="none" stroke="#12b0e8" stroke-width="1.8"><circle cx="12" cy="12" r="9"/><ellipse cx="12" cy="12" rx="4" ry="9"/><path d="M3 12h18M5 7h14M5 17h14"/></g></svg>
          www.vitalsparkelectrical-example.com.au
        </li>
      </ul>
    </div>
    <div class="accent-line"></div>
    <p class="licence">R.E.C 57318</p>
    <div class="accent-line accent-line--end"></div>
  </section>
</main>
</body>
</html>
```